Tidewell Recovery Business Card Design

Professional and clean design. The design colors should flow with the logo. Two-sided card with the website on the back which is:

www.TidewellRecovery.example.

"Specializing in Water Damage Restoration"

On the front I need the name, email, phone, and logo.

Name: Dorian Vashti
Email: Dorian@TidewellRecovery.example
Phone: 555-318-2046 for now

I only have the Preview and Thumbnail right now but should have the source files uploaded within a day or two.

Target Market(s)

Flood victims, home owners with water damage from busted pipes etc...

Industry/Entity Type

Business

Contact Information for Business Card

Name: Dorian Vashti

Font styles to use
Serif
Sans Serif

```html
<!DOCTYPE html>
<html lang="en">
<head>
<meta charset="utf-8">
<title>Tidewell Recovery Business Card</title>
<link rel="stylesheet" href="https://fonts.googleapis.com/css2?family=Open+Sans:wght@400;600&display=swap">
<style>
  :root {
    --page-bg: #e9ebee;
    --card-bg: #f7f9fb;
    --brand-blue: #1f6fb8;
    --wave-dark: #1b62ad;
    --wave-mid: #2f8fd6;
    --wave-light: #5fb0e6;
    --text-grey: #454a50;
    --rule-grey: #8a8f95;
    --faint-mark: #dfe7ef;
  }
  html, body {
    margin: 0;
    padding: 0;
    width: 1200px;
    height: 970px;
    overflow: hidden;
    background: var(--page-bg);
    font-family: "Open Sans", Arial, sans-serif;
  }
  .business-card {
    position: absolute;
    left: 100px;
    top: 207px;
    width: 1000px;
    height: 556px;
    background: var(--card-bg);
    border-radius: 22px;
    overflow: hidden;
    box-shadow: 0 10px 30px rgba(0,0,0,0.12);
  }
  .faint-circle {
    position: absolute;
    left: 545px;
    top: 48px;
    width: 460px;
    height: 460px;
    border-radius: 50%;
    border: 14px solid var(--faint-mark);
    box-sizing: border-box;
  }
  .brand {
    position: absolute;
    left: 48px;
    top: 40px;
    width: 420px;
    text-align: center;
  }
  .brand-dot {
    width: 120px;
    height: 120px;
    margin: 0 auto 18px;
    border-radius: 50%;
    background: var(--brand-blue);
  }
  .brand-name {
    margin: 0;
    font-size: 40px;
    font-weight: 600;
    color: var(--brand-blue);
    letter-spacing: 1px;
    white-space: nowrap;
  }
  .divider {
    position: absolute;
    left: 48px;
    top: 336px;
    width: 622px;
    height: 2px;
    background: var(--rule-grey);
  }
  .person-name {
    position: absolute;
    left: 684px;
    top: 316px;
    margin: 0;
    font-size: 28px;
    font-weight: 600;
    color: var(--brand-blue);
    white-space: nowrap;
  }
  .contact-list {
    position: absolute;
    left: 48px;
    top: 360px;
    margin: 0;
    padding: 0;
    list-style: none;
  }
  .contact-item {
    display: flex;
    align-items: center;
    height: 35.5px;
    font-size: 22px;
    color: var(--text-grey);
    white-space: nowrap;
  }
  .contact-icon {
    width: 22px;
    height: 22px;
    margin-right: 12px;
    fill: var(--text-grey);
  }
  .wave-band {
    position: absolute;
    left: 0;
    bottom: 0;
    width: 1000px;
    height: 110px;
  }
</style>
</head>
<body>
  <div class="business-card">
    <div class="faint-circle"></div>

    <div class="brand">
      <div class="brand-dot"></div>
      <p class="brand-name">Tidewell Recovery</p>
    </div>

    <div class="divider"></div>
    <p class="person-name">Dorian Vashti</p>

    <ul class="contact-list">
      <li class="contact-item">
        <svg class="contact-icon" viewBox="0 0 24 24" aria-hidden="true"><path d="M6.6 10.8c1.4 2.8 3.8 5.1 6.6 6.6l2.2-2.2c.3-.3.7-.4 1-.2 1.1.4 2.3.6 3.6.6.6 0 1 .4 1 1V20c0 .6-.4 1-1 1C10.6 21 3 13.4 3 4c0-.6.4-1 1-1h3.5c.6 0 1 .4 1 1 0 1.3.2 2.5.6 3.6.1.3 0 .7-.2 1L6.6 10.8z"/></svg>
        555-318-2046
      </li>
      <li class="contact-item">
        <svg class="contact-icon" viewBox="0 0 24 24" aria-hidden="true"><path d="M3 5h18v14H3z M3 5l9 7 9-7" fill="none" stroke="#454a50" stroke-width="2"/></svg>
        Dorian@TidewellRecovery.example
      </li>
      <li class="contact-item">
        <svg class="contact-icon" viewBox="0 0 24 24" aria-hidden="true"><circle cx="12" cy="12" r="9" fill="none" stroke="#454a50" stroke-width="2"/><path d="M3 12h18M12 3c3 3 3 15 0 18M12 3c-3 3-3 15 0 18" fill="none" stroke="#454a50" stroke-width="1.6"/></svg>
        www.TidewellRecovery.example
      </li>
    </ul>

    <svg class="wave-band" viewBox="0 0 1000 110" preserveAspectRatio="none" aria-hidden="true">
      <path d="M0 30 C 160 60, 300 70, 480 58 C 680 44, 820 10, 1000 18 L1000 110 L0 110 Z" fill="var(--wave-mid)"/>
      <path d="M0 56 C 180 82, 360 84, 560 66 C 740 50, 880 38, 1000 42 L1000 110 L0 110 Z" fill="var(--wave-light)" opacity="0.55"/>
      <path d="M0 14 C 160 44, 300 58, 480 46 C 680 32, 820 0, 1000 6" fill="none" stroke="var(--wave-dark)" stroke-width="7"/>
      <path d="M0 44 C 140 68, 260 76, 420 66" fill="none" stroke="#ffffff" stroke-width="4"/>
    </svg>
  </div>
</body>
</html>
```